Flyer-Design für Dekorations- und Farbkonzepte
hat alles bestens geklappt und tolles Design...kann Sie nur weiterempfehlen! PS. Lieben Dank für die Geduld! Beste Grüsse Sabrina Lüthold
Zielgruppe
Dekorationskonzepte, Farbkonzepte für Räume, Planung und Realisation Geschäfts - und Privatkunden, Zielgruppe Firmen, Seniorenheime , Privatkundschaft
Aufgabenstellung
Ich bin im Mai an einem Anlass in einem Seniorenheim und habe die Möglichkeit mich zu präsentieren , ich mache an diesem Anlass die Dekoration und möchte dabei Tag einen wertigen Flyer abgeben. An diesem Anlass sind auch der Gemeindepräsident und Angehörige der Bewohner etc . eingeladen. Der Flyer soll etwas gediegen daherkommen und über meine Arbeit informieren. Ich möchte vorallem Geschäftskunden ansprechen. Der Flyer sollte Emotionen wecken. Masse ca. A5 ..bin da sehr offen (nicht zu klein )

```html
<!DOCTYPE html>
<html lang="de">
<head>
<meta charset="utf-8">
<title>Ihre Räume sind Ihre Visitenkarte</title>
<link rel="stylesheet" href="https://fonts.googleapis.com/css2?family=Encode+Sans+Compressed:wght@200&family=Fira+Sans+Extra+Condensed:wght@300&display=swap">
<style>
  :root {
    --page: #ffffff;
    --panel: #7a8ea5;
    --ink: #ffffff;
  }
  html, body {
    margin: 0;
    padding: 0;
    width: 846px;
    height: 1200px;
    overflow: hidden;
    background: var(--page);
  }
  .flyer {
    position: relative;
    width: 846px;
    height: 1200px;
  }
  .panel {
    position: absolute;
    left: 28px;
    top: 28px;
    width: 771px;
    height: 1123px;
    background: var(--panel);
  }
  .hero-image {
    position: absolute;
    left: 71px;
    top: 85px;
    width: 682px;
    height: 356px;
    display: block;
  }
  .headline {
    position: absolute;
    left: 74px;
    top: 472px;
    margin: 0;
    font-family: "Encode Sans Compressed", sans-serif;
    font-weight: 200;
    font-size: 58px;
    line-height: 69px;
    letter-spacing: 4.5px;
    color: var(--ink);
    text-transform: uppercase;
    white-space: nowrap;
  }
  .intro {
    position: absolute;
    left: 75px;
    top: 621px;
    width: 690px;
    margin: 0;
    font-family: "Fira Sans Extra Condensed", sans-serif;
    font-weight: 300;
    font-size: 23.2px;
    line-height: 33.2px;
    color: var(--ink);
    white-space: nowrap;
  }
  .divider {
    position: absolute;
    left: 75px;
    top: 1031px;
    width: 681px;
    height: 3px;
    background: var(--ink);
  }
</style>
</head>
<body>
<div class="flyer">
  <div class="panel"></div>

  <svg class="hero-image" viewBox="0 0 682 356" role="img" aria-label="Foto eines Wohnraums: hellgraues Sofa mit Kissen vor weißer Ziegelwand, goldene Laternen, zwei runde Holztischchen und eine Pendelleuchte auf dunklem Holzboden">
    <defs>
      <linearGradient id="room-tone" x1="0" y1="0" x2="0" y2="1">
        <stop offset="0" stop-color="#ebe8e4"/>
        <stop offset="0.78" stop-color="#d9d6d2"/>
        <stop offset="0.8" stop-color="#4a3b30"/>
        <stop offset="1" stop-color="#2f251f"/>
      </linearGradient>
    </defs>
    <rect width="682" height="356" fill="url(#room-tone)"/>
  </svg>

  <h1 class="headline">Ihre Räume sind<br>Ihre Visitenkarte</h1>

  <p class="intro">Es gibt keine zweite Chance für den ersten Eindruck. Was für den persönlichen<br>
Auftritt gilt, gilt auch für die Räume Ihres Geschäfts. Kunden, Partner, Patienten,<br>
Besucher oder Gäste entscheiden in den ersten Momenten, ob sie sich bei Ihnen<br>
wohlfühlen. Und ob sie wiederkommen. Anders formuliert: Mit einer durchdach-<br>
ten, einladenden und stimmigen Einrichtung haben Sie ein für Ihre Kundschaft<br>
zwar meist unbewusstes, aber wirkungsvolles Verkaufsinstrument in der Hand,<br>
das tiefer geht als ein gelungener Webauftritt. Ich zeige Ihnen gerne, wie Sie aus<br>
Eingangsbereichen, Wartezimmern, Studios, Praxen und anderen Bereichen Ihres<br>
Geschäfts wahre Wohlfühlzonen kreieren. Sehen, riechen, hören, fühlen – auf der<br>
Ebene der Emotionen bringen Sie das Image und die Markenwerte Ihres Unter-<br>
nehmens direkt an Ihre Zielgruppe. Sie werden sehen – es lohnt sich!</p>

  <div class="divider"></div>
</div>
</body>
</html>
```